Vacation rental Management Software company needs website and logo

We need a logo and new website design to promote our vacation rental management software. We sell the software to property owners and management company. We have existing website www.stayquill.example at the moment but it is need of upgrading. The goal is make it more professional looking and to put the emphasis on marketing the software.
Html + Css code is needed, the website must have responsive layout.
The logo must be composed by the brand "StayQuill" and eventually an image related to Vacation Rental Management
The pages that we need are the following:
1) Home Page
- must be highlighted the 2 main categories of customers (Direct Owners and Agencies/Portals)
- there must be a section where we can highlight some products, i.e. the latest or the most relevant
- there must be an introductive text
2) Page for a category of customer (owner or agency/portal)
- based on the page http://www.stayquill.example/owners/ or http://www.stayquill.example/agencies/, this page must highlight all the products available for the category selected, but must be more attractive then the existing ones (that have just text)
3) Single product page
- in that page must be explained a single product, a page example is this one: http://www.stayquill.example/owners/vacation-rental-website.html
4) Portfolio page
5) Contact page, with a contact form style
Industry/Entity Type
Software

```html
<!DOCTYPE html>
<html lang="en">
<head>
<meta charset="utf-8">
<title>StayQuill – Villa Rentals Booking Solutions</title>
<link href="https://fonts.googleapis.com/css2?family=Oxygen:wght@400;700&family=Arimo:ital,wght@0,400;0,700;1,400&display=swap" rel="stylesheet">
<style>
  :root{
    --red:#b30d0d;
    --text:#333333;
    --muted:#666666;
    --light:#8a8a8a;
    --panel-dark:#474747;
    --panel-mid:#5c5c5c;
    --panel-light:#737373;
    --rule:#d6d6d6;
    --footer:#f0f0f0;
    --white:#ffffff;
  }
  *{box-sizing:border-box;margin:0;padding:0}
  html,body{width:1128px;height:1200px;overflow:hidden;background:var(--white)}
  body{font-family:"Arimo",Arial,sans-serif;color:var(--text);position:relative}
  a{color:inherit;text-decoration:none}
  .wrap{position:absolute;left:160px;width:808px}

  /* header */
  .site-header{top:30px;height:70px}
  .brand{position:absolute;left:0;top:10px;display:flex;align-items:center;gap:10px}
  .brand-mark{width:26px;height:26px;background:var(--red)}
  .brand-text{display:flex;flex-direction:column}
  .brand-name{font-family:"Oxygen",sans-serif;font-weight:700;font-size:28px;color:var(--red);line-height:1}
  .brand-tag{font-size:9px;color:var(--text);margin-top:3px}
  .lang{position:absolute;right:0;top:3px;width:81px;height:22px;border:1px solid #c9c9c9;font-size:9px;display:flex;align-items:center;padding-left:8px;gap:6px}
  .lang-flag{width:15px;height:10px;background:#2b3f8a}
  .lang svg{position:absolute;right:6px;top:8px}
  .main-nav{position:absolute;right:2px;top:44px;display:flex;gap:66px;font-size:11px;color:var(--text)}

  /* hero */
  .hero{top:111px;height:332px;background:linear-gradient(180deg,#8a6f5e 0%,#c7936a 40%,#b2642a 70%,#3a2416 100%)}
  .hero-bar{position:absolute;left:0;right:0;bottom:0;height:47px;background:rgba(0,0,0,.62);display:flex;align-items:center;padding-left:23px}
  .hero-title{font-family:"Oxygen",sans-serif;font-size:15px;color:var(--white)}
  .hero-arrows{position:absolute;right:12px;top:16px;display:flex;gap:2px}
  .hero-arrows span{width:17px;height:17px;background:#d2321f;display:flex;align-items:center;justify-content:center}

  /* audience boxes */
  .audience{top:456px;height:125px;display:flex;gap:1px}
  .audience-card{flex:1;position:relative;color:var(--white);padding:26px 0 0 102px}
  .audience-card.owners{background:var(--panel-dark)}
  .audience-card.agencies{background:var(--panel-mid);padding-left:94px}
  .audience-card.login{background:var(--panel-light);padding-left:102px}
  .audience-card svg{position:absolute;left:32px;top:32px}
  .audience-card h3{font-family:"Oxygen",sans-serif;font-weight:400;font-size:13px;margin-bottom:9px}
  .audience-card p{font-size:9px;line-height:18.5px;color:#d0d0d0;width:150px}
  .audience-card .link{display:block;font-size:11.5px;text-decoration:underline;margin-bottom:9px}

  /* about + testimonials */
  .section-title{font-family:"Oxygen",sans-serif;font-weight:700;font-size:12.5px;color:var(--red);letter-spacing:-.2px}
  .about{top:612px;width:440px}
  .about h2{margin-left:2px}
  .about .lead{font-size:12px;margin:13px 0 12px 2px}
  .about-body{display:flex;gap:24px}
  .about-photo{width:186px;height:128px;background:linear-gradient(135deg,#c9ccd1,#3f4654 60%,#e8e2dc)}
  .about-text{width:220px;font-size:9px;line-height:17.6px;color:var(--text);padding-top:1px}
  .read-more{display:block;color:var(--red);margin-top:7px}

  .testimonials{top:612px;left:626px;width:342px}
  .testimonials .arrows{position:absolute;right:10px;top:2px}
  .quote-box{position:relative;margin-top:19px;height:109px;border:1px solid #d9d9d9;border-radius:8px;background:#f6f6f6;padding:24px 50px 0 49px;font-size:9px;line-height:17.6px}
  .quote-box .q{position:absolute;font-family:Georgia,serif;font-size:26px;color:#c4c4c4;font-style:italic}
  .quote-box svg.tail{position:absolute;left:194px;bottom:-23px}
  .author{margin:21px 0 0 12px;font-size:9.5px;color:var(--red)}
  .posted{margin:6px 0 0 12px;font-size:9.5px;font-style:italic;color:var(--text)}

  .divider{top:832px;height:1px;background:var(--rule)}

  /* products */
  .products{top:848px}
  .products .arrows{position:absolute;right:2px;top:4px}
  .product-grid{display:flex;gap:30px;margin-top:23px}
  .product{width:178px}
  .product-photo{height:110px}
  .product h4{font-family:"Oxygen",sans-serif;font-weight:700;font-size:10.5px;color:var(--red);margin:15px 0 8px 1px;letter-spacing:-.2px}
  .product p{font-size:9.5px;font-style:italic;color:var(--text);margin-left:1px}

  /* footer */
  .site-footer{top:1070px;height:66px;background:linear-gradient(180deg,#ececec,#fbfbfb)}
  .footer-nav{position:absolute;left:29px;top:21px;display:flex;gap:27px;font-size:9.5px;color:var(--muted)}
  .copyright{position:absolute;left:29px;top:47px;font-size:9.5px;color:var(--muted)}
  .follow{position:absolute;right:20px;top:28px;display:flex;align-items:center;gap:8px;font-size:9.5px;color:var(--muted)}
  .follow span.dot{width:26px;height:26px;border-radius:50%;background:#b8b8b8}
  .follow .label{margin-right:1px}
</style>
</head>
<body>

<header class="wrap site-header">
  <a class="brand" href="#">
    <span class="brand-mark"></span>
    <span class="brand-text">
      <span class="brand-name">StayQuill</span>
      <span class="brand-tag">Villa Rentals Booking Solutions</span>
    </span>
  </a>
  <div class="lang"><span class="lang-flag"></span>English
    <svg width="7" height="5" viewBox="0 0 7 5"><path d="M0.5 0.5 3.5 3.5 6.5 0.5" fill="none" stroke="#555"/></svg>
  </div>
  <nav class="main-nav">
    <a href="#">Home</a><a href="#">Products &amp; Services</a><a href="#">Portfolio</a><a href="#">Owners</a><a href="#">Contact Us</a>
  </nav>
</header>

<section class="wrap hero" role="img" aria-label="City skyline of tall towers at sunset">
  <div class="hero-bar">
    <h1 class="hero-title">THE RIGHT WAY TO MANAGE RESERVATIONS</h1>
    <div class="hero-arrows">
      <span><svg width="6" height="9" viewBox="0 0 6 9"><path d="M5 0.5 1 4.5 5 8.5" fill="none" stroke="#fff"/></svg></span>
      <span><svg width="6" height="9" viewBox="0 0 6 9"><path d="M1 0.5 5 4.5 1 8.5" fill="none" stroke="#fff"/></svg></span>
    </div>
  </div>
</section>

<section class="wrap audience">
  <div class="audience-card owners">
    <svg width="48" height="58" viewBox="0 0 48 58"><circle cx="24" cy="14" r="12" fill="#d9d9d9"/><path d="M2 56 Q2 30 24 30 Q46 30 46 56 Z" fill="#d9d9d9"/><path d="M22 32 L26 32 L27 50 L24 54 L21 50 Z" fill="#474747"/></svg>
    <h3>DIRECT OWNERS</h3>
    <p>The easiest and cheapest way to collect the rent amounts and to manage the security deposits</p>
  </div>
  <div class="audience-card agencies">
    <svg width="50" height="40" viewBox="0 0 50 40" style="left:27px;top:45px"><path d="M2 8 L16 4 L26 10 L36 4 L48 8 L48 22 L38 32 L28 38 L12 28 L2 22 Z" fill="#d9d9d9"/><path d="M16 18 L28 28 M22 14 L34 24" stroke="#5c5c5c" stroke-width="2"/></svg>
    <h3>AGENCIES AND PORTALS</h3>
    <p>The easiest and cheapest way to collect the rent amounts and to manage the security deposits</p>
  </div>
  <div class="audience-card login">
    <svg width="52" height="52" viewBox="0 0 52 52" style="left:30px;top:35px"><circle cx="26" cy="26" r="25" fill="#e6e6e6"/><path d="M15 27 L23 35 L38 18" fill="none" stroke="#737373" stroke-width="6"/></svg>
    <h3>LOGIN</h3>
    <a class="link" href="#">Owners login</a>
    <a class="link" href="#">Register Now</a>
  </div>
</section>

<section class="wrap about">
  <h2 class="section-title">ABOUT STAYQUILL</h2>
  <p class="lead">Professional Vacation &amp; Villa Rental Management Software</p>
  <div class="about-body">
    <div class="about-photo" role="img" aria-label="Business team reviewing work at a laptop"></div>
    <div class="about-text">StayQuill has the best solutions for managing every aspect of villa and vacation rental homes. Built from the ground up around the industry, it is designed to deal with all the day-to-day operations of booking, managing reservations, customer service, communications with clients...
      <a class="read-more" href="#">[ Read More + ]</a>
    </div>
  </div>
</section>

<section class="wrap testimonials">
  <h2 class="section-title">TESTIMONIALS</h2>
  <svg class="arrows" width="20" height="8" viewBox="0 0 20 8"><path d="M4 0.5 1 4 4 7.5" fill="none" stroke="#3a7bd5"/><path d="M16 0.5 19 4 16 7.5" fill="none" stroke="#777"/></svg>
  <div class="quote-box">
    <span class="q" style="left:20px;top:10px">&ldquo;</span>
    StayQuill has the best solutions for managing every aspect of villa and vacation rental homes. Built from the ground up around the industry, it is designed to deal...
    <span class="q" style="right:14px;top:68px">&rdquo;</span>
    <svg class="tail" width="50" height="24" viewBox="0 0 50 24"><path d="M0 0 L2 23 L48 0" fill="#f6f6f6" stroke="#d9d9d9"/><path d="M1 -1 L47 -1" stroke="#f6f6f6" stroke-width="2"/></svg>
  </div>
  <p class="author">Marcus Ellery</p>
  <p class="posted">Posted on 27 March 2014</p>
</section>

<div class="wrap divider"></div>

<section class="wrap products">
  <h2 class="section-title">LATEST PRODUCTS</h2>
  <svg class="arrows" width="20" height="8" viewBox="0 0 20 8"><path d="M4 0.5 1 4 4 7.5" fill="none" stroke="#999"/><path d="M16 0.5 19 4 16 7.5" fill="none" stroke="#999"/></svg>
  <div class="product-grid">
    <div class="product">
      <div class="product-photo" role="img" aria-label="Hands typing on a laptop keyboard" style="background:linear-gradient(135deg,#dfe6ee,#9aa6b4 55%,#5a6470)"></div>
      <h4>EASY RESERVE</h4><p>Click here for more Info</p>
    </div>
    <div class="product">
      <div class="product-photo" role="img" aria-label="Hand holding a small model house and keys" style="background:linear-gradient(135deg,#f2f2f2,#d8c2b2 55%,#c0c6cf)"></div>
      <h4>TUSCANY VILLAS</h4><p>Click here for more Info</p>
    </div>
    <div class="product">
      <div class="product-photo" role="img" aria-label="White villa with porch and green lawn" style="background:linear-gradient(180deg,#9fc1e4,#e8ecef 45%,#6f8f4e)"></div>
      <h4>ITALY VILLAS</h4><p>Click here for more Info</p>
    </div>
    <div class="product">
      <div class="product-photo" role="img" aria-label="Handshake in front of a house" style="background:linear-gradient(135deg,#2b2b2b,#c9a48a 45%,#8fb0d8)"></div>
      <h4>WANDERKEYS</h4><p>Click here for more Info</p>
    </div>
  </div>
</section>

<footer class="wrap site-footer">
  <nav class="footer-nav">
    <a href="#">Home</a><a href="#">Products &amp; Services</a><a href="#">Portfolio</a><a href="#">Owners</a><a href="#">Contact Us</a>
  </nav>
  <p class="copyright">Copyright © 2014 StayQuill. All Rights Reserved.</p>
  <div class="follow"><span class="label">Follow Us :</span><span class="dot"></span><span class="dot"></span><span class="dot"></span><span class="dot"></span></div>
</footer>

</body>
</html>
```